Quimby's Yard & Garden Center Business Card Update

I need an updated Business card design for my Lawn and Garden Center. We do Landscaping installs, Lawn Mowing, Snow Removal and also have a Garden Center Retail Division. I uploaded a few of our previous business cards to give an idea of what we are starting with. The main goal of this update is to simplify and modernize the business card, not all of the services that are on the previous cards has to be on the new one but I would still like to highlight our main services. There is also a sample of our logo that Can be used in the design.

Industry/Entity Type

Landscaping

Contact Information for Business Card

Morris Quimby
Morris@Quimbysyardandgarden.example
Business (555) 201-7784
Cell (555) 318-6092

Colors

Designer to choose colors to be used in the design.

Requirements
Must have
• Services Provided :
• Landscaping
• Lawn Maintenance
• Snow Removal
• Garden Center

```html
<!DOCTYPE html>
<html lang="en">
<head>
<meta charset="UTF-8">
<title>Quimby's Yard &amp; Garden Center – Business Card</title>
<link rel="stylesheet" href="https://fonts.googleapis.com/css2?family=Bebas+Neue&family=Poppins:wght@400;600&display=swap">
<style>
  :root {
    --paper: #ffffff;
    --paper-shade: #ececec;
    --ink: #2b2b2b;
    --bar: #262626;
    --forest: #2d5129;
    --leaf: #0f8f45;
    --frame: #444444;
    --white: #ffffff;
    --white-soft: rgba(255, 255, 255, 0.85);
  }
  html, body {
    margin: 0;
    padding: 0;
    overflow: hidden;
    background: var(--paper);
  }
  .card {
    position: relative;
    width: 1200px;
    height: 686px;
    overflow: hidden;
    background: linear-gradient(135deg, var(--paper) 0%, var(--paper-shade) 45%, var(--paper) 70%, var(--paper-shade) 100%);
  }
  .card-shapes {
    position: absolute;
    inset: 0;
    width: 1200px;
    height: 686px;
  }
  .holder-name {
    position: absolute;
    left: 91px;
    top: 112px;
    margin: 0;
    font-family: "Bebas Neue", sans-serif;
    font-weight: 400;
    font-size: 86px;
    line-height: 1;
    letter-spacing: 0.5px;
    color: var(--white);
  }
  .holder-name .surname { color: var(--leaf); }
  .brand-name {
    position: absolute;
    left: 790px;
    top: 228px;
    width: 350px;
    text-align: center;
    font-family: "Poppins", sans-serif;
    font-weight: 600;
    font-size: 58px;
    color: var(--white);
    line-height: 1;
  }
  .service-list {
    position: absolute;
    left: 790px;
    top: 318px;
    width: 350px;
    margin: 0;
    padding: 16px 0 0;
    list-style: none;
    border-top: 2px solid var(--leaf);
    text-align: center;
    font-family: "Poppins", sans-serif;
    font-weight: 400;
    font-size: 19px;
    line-height: 32px;
    letter-spacing: 1.5px;
    text-transform: uppercase;
    color: var(--white-soft);
  }
  .contact-list {
    list-style: none;
    margin: 0;
    padding: 0;
  }
  .contact-item {
    position: absolute;
    left: 90px;
    display: flex;
    align-items: center;
  }
  .contact-icon {
    width: 62px;
    height: 62px;
    flex: none;
  }
  .contact-text {
    margin-left: 22px;
    font-family: "Poppins", sans-serif;
    font-size: 23px;
    line-height: 31px;
    color: var(--ink);
  }
  .contact-address { top: 364px; }
  .contact-phone { top: 457px; }
  .contact-web { top: 548px; }
</style>
</head>
<body>
<div class="card">
  <svg class="card-shapes" viewBox="0 0 1050 600" preserveAspectRatio="none" aria-hidden="true">
    <path d="M0 77 H545 Q562 77 558 93 L532 190 Q528 203 514 203 H0 Z" fill="var(--bar)"/>
    <path d="M677 0 H1050 V580 L632 470 Q562 452 580 385 Z" fill="var(--forest)"/>
    <path d="M574 -10 L567 36 Q564 48 576 51 L812 111 Q824 114 827 102 L852 -10" fill="none" stroke="var(--frame)" stroke-width="5" stroke-linejoin="round"/>
    <path d="M853 610 L877 479 Q880 465 894 468 L1060 510" fill="none" stroke="var(--frame)" stroke-width="5" stroke-linejoin="round"/>
  </svg>

  <h1 class="holder-name">Morris <span class="surname">Quimby</span></h1>

  <div class="brand-name">Quimby's</div>

  <ul class="service-list">
    <li>Landscaping</li>
    <li>Lawn Maintenance</li>
    <li>Snow Removal</li>
    <li>Garden Center</li>
  </ul>

  <ul class="contact-list">
    <li class="contact-item contact-address">
      <svg class="contact-icon" viewBox="0 0 62 62" aria-hidden="true">
        <circle cx="31" cy="31" r="27" fill="var(--white)" stroke="var(--leaf)" stroke-width="4.5"/>
        <path d="M31 19 C25 19 21.5 23.5 21.5 28 C21.5 34 31 44 31 44 C31 44 40.5 34 40.5 28 C40.5 23.5 37 19 31 19 Z" fill="var(--ink)"/>
        <circle cx="31" cy="28" r="3.6" fill="var(--white)"/>
      </svg>
      <span class="contact-text">4820 MEADOW LANE ROAD, FERNVALE,<br>OHIO 45999, UNITED STATES</span>
    </li>
    <li class="contact-item contact-phone">
      <svg class="contact-icon" viewBox="0 0 62 62" aria-hidden="true">
        <circle cx="31" cy="31" r="27" fill="var(--white)" stroke="var(--leaf)" stroke-width="4.5"/>
        <path d="M22 19 L27 19 L29.5 25.5 L26.5 28 C28 31.5 30.5 34 34 35.5 L36.5 32.5 L43 35 L43 40 C43 42 41 43.5 39 43 C29 41 21 33 19 23 C18.5 21 20 19 22 19 Z" fill="var(--ink)"/>
      </svg>
      <span class="contact-text">(555) 201-7784<br>(555) 318-6092</span>
    </li>
    <li class="contact-item contact-web">
      <svg class="contact-icon" viewBox="0 0 62 62" aria-hidden="true">
        <circle cx="31" cy="31" r="27" fill="var(--white)" stroke="var(--leaf)" stroke-width="4.5"/>
        <g fill="none" stroke="var(--ink)" stroke-width="2.4">
          <circle cx="31" cy="31" r="11.5" fill="var(--ink)"/>
          <ellipse cx="31" cy="31" rx="4.5" ry="11.5" stroke="var(--white)" stroke-width="1.6"/>
          <line x1="19.5" y1="31" x2="42.5" y2="31" stroke="var(--white)" stroke-width="1.6"/>
          <line x1="21" y1="25.5" x2="41" y2="25.5" stroke="var(--white)" stroke-width="1.4"/>
          <line x1="21" y1="36.5" x2="41" y2="36.5" stroke="var(--white)" stroke-width="1.4"/>
        </g>
      </svg>
      <span class="contact-text">Morris@Quimbysyardandgarden.example</span>
    </li>
  </ul>
</div>
</body>
</html>
```